Legal Service Estimated Retainer and Average Case Value

We need an 11x14 flyer that contains the standard retainers and average cost be case, both provided in documents, for each case type we handle. We need the information displayed, preferably in a way that makes the information readable but less troubling to a client shocked at price of litigation. We need one sheet with the retainers and average case value merged into one table.

Target Market(s)

Potential Clients

Font styles to use
Serif
Sans Serif

```html
<!DOCTYPE html>
<html lang="en">
<head>
<meta charset="utf-8">
<title>Retainers and Average Fees by Case Type</title>
<link href="https://fonts.googleapis.com/css2?family=Fira+Sans:wght@400;600&display=swap" rel="stylesheet">
<style>
  :root {
    --header-bg: #3d3a5c;
    --row-grey: #6d6e70;
    --row-white: #ffffff;
    --ink-dark: #1d1d2a;
    --ink-light: #ffffff;
    --navy: #14173f;
    --brand-navy: #1b2152;
    --sky-top: #eef3f8;
    --sky-mid: #d6e0ee;
    --suit-blue: #8d9ad6;
  }
  * { box-sizing: border-box; margin: 0; padding: 0; }
  html, body { width: 1200px; height: 943px; overflow: hidden; background: #fff; }
  body { font-family: "Fira Sans", sans-serif; position: relative; }

  .hero-backdrop {
    position: absolute; left: 0; top: 0; width: 1200px; height: 807px;
    background:
      linear-gradient(90deg, rgba(141,154,214,0.55) 0%, rgba(141,154,214,0.35) 22%, rgba(255,255,255,0) 30%),
      linear-gradient(180deg, var(--sky-mid) 0%, var(--sky-top) 55%, #f6f4f3 100%);
  }

  .fee-table {
    position: absolute; left: 299px; top: 46px; width: 851px;
    border-collapse: collapse; table-layout: fixed;
  }
  .fee-table col.case-col { width: 305px; }
  .fee-table col.retainer-col { width: 282px; }
  .fee-table col.fee-col { width: 264px; }
  .fee-table th {
    background: var(--header-bg); color: var(--ink-light);
    font-weight: 600; font-size: 18px; line-height: 20px;
    height: 52px; text-align: center; letter-spacing: 0.2px;
  }
  .fee-table td {
    height: 51.3px; font-size: 15.5px; line-height: 18px;
    letter-spacing: 0.2px;
  }
  .fee-table td.case-type { padding-left: 5px; text-align: left; }
  .fee-table td.retainer, .fee-table td.avg-fee { text-align: center; }
  .fee-table tr.row-grey td { background: var(--row-grey); color: var(--ink-light); }
  .fee-table tr.row-white td { background: var(--row-white); color: var(--ink-dark); }
  .fee-table tr.row-last td { height: 57px; }

  .brand {
    position: absolute; left: 14px; top: 848px;
    display: flex; align-items: center; gap: 12px;
  }
  .brand-mark { width: 40px; height: 40px; background: var(--brand-navy); }
  .brand-name {
    color: var(--brand-navy); font-weight: 600; font-size: 17px; line-height: 21px;
    letter-spacing: 0.4px; text-transform: uppercase;
  }

  .disclaimer {
    position: absolute; left: 429px; top: 807px; width: 771px; height: 136px;
    background: var(--navy); color: var(--ink-light);
    padding: 20px 24px 0 28px;
    font-size: 16.6px; line-height: 20px; letter-spacing: 0.15px;
  }
</style>
</head>
<body>
  <div class="hero-backdrop" role="img" aria-label="Photograph of a man in a blue suit and sunglasses walking down white stone steps with a leather briefcase"></div>

  <table class="fee-table">
    <colgroup><col class="case-col"><col class="retainer-col"><col class="fee-col"></colgroup>
    <thead>
      <tr><th>Case type</th><th>Retainers &amp; Estimated<br>Case Cost</th><th>Average Fee Per Case Type</th></tr>
    </thead>
    <tbody>
      <tr class="row-grey"><td class="case-type">(PTA) Protection from Abuse</td><td class="retainer">$2,000&nbsp; (Paid in full)</td><td class="avg-fee">$1,500 - $3,000</td></tr>
      <tr class="row-white"><td class="case-type">Divorce (3301 C)</td><td class="retainer">$2,000</td><td class="avg-fee">$1,500 - $3,000</td></tr>
      <tr class="row-grey"><td class="case-type">Divorce (3301 D)</td><td class="retainer">$2,500</td><td class="avg-fee">$2,000 - $3,000</td></tr>
      <tr class="row-white"><td class="case-type">Divorce &amp; Support</td><td class="retainer">$3,000</td><td class="avg-fee">$2,000 - $4,000</td></tr>
      <tr class="row-grey"><td class="case-type">Divorce &amp; Custody</td><td class="retainer">$3,500</td><td class="avg-fee">$5,000 - $8,000</td></tr>
      <tr class="row-white"><td class="case-type">Divorce &amp; Equitable Distribution</td><td class="retainer">$3,500</td><td class="avg-fee">$6,000 - $10,000</td></tr>
      <tr class="row-grey"><td class="case-type">Divorce, Custody &amp; Support</td><td class="retainer">$3,500</td><td class="avg-fee">$8,000 - $12,000</td></tr>
      <tr class="row-white"><td class="case-type">Divorce, Equitable Distribution &amp; Support</td><td class="retainer">$3,500</td><td class="avg-fee">$8,000 - $12,000</td></tr>
      <tr class="row-grey"><td class="case-type">Divorce, Equitable Distribution &amp; Custody</td><td class="retainer">$5,000</td><td class="avg-fee">$10,000 - $15,000</td></tr>
      <tr class="row-white"><td class="case-type">Divorce, Equitable Distribution, Custody<br>&amp; Support</td><td class="retainer">$3,500</td><td class="avg-fee">$12,000 - $15,000</td></tr>
      <tr class="row-grey"><td class="case-type">Custody Initial Order</td><td class="retainer">$3,000</td><td class="avg-fee">$4,000 - $7,000</td></tr>
      <tr class="row-white"><td class="case-type">Custody &amp; Support</td><td class="retainer">$3,000</td><td class="avg-fee">$5,000 - $8,000</td></tr>
      <tr class="row-grey row-last"><td class="case-type">Custody Modification</td><td class="retainer">$3,500</td><td class="avg-fee">$5,000 - $8,000</td></tr>
    </tbody>
  </table>

  <div class="brand">
    <div class="brand-mark"></div>
    <div class="brand-name">The Law Office of<br>Daniel M Whitfield</div>
  </div>

  <div class="disclaimer">
    In order for our clients to set expectations for legal fees, we provide the national average range of fees per case type. These are only to provide you with an understanding of what other cases have cost clients in similar cases. Please note these are not estimates nor guarantees of your own legal costs.
  </div>
</body>
</html>
```